Houston Law Firm Business Card
Taven & Associates, PC 2013 Business Card
Professional
Dorian M. Taven
Trial Attorney
482 W. Birchfield Ave.
Suite 318
Houston, TX 77391
1-888-50-TAVEN
dorian.taven@tavenassociateslaw.example
tavenassociateslaw.example
Also include my blog:
lakeridgetrialcounsel.example

```html
<!DOCTYPE html>
<html lang="en">
<head>
<meta charset="utf-8">
<title>Taven &amp; Associates, PC — Business Card</title>
<link rel="stylesheet" href="https://fonts.googleapis.com/css2?family=Cinzel:wght@500&family=Open+Sans:wght@400;600&display=swap">
<style>
  :root {
    --backdrop: #d9d8d3;
    --card: #ffffff;
    --olive-dark: #4a4634;
    --olive: #6e6847;
    --olive-light: #a39d7c;
    --text: #5e5b52;
    --text-soft: #85827a;
    --rule: #c9c6ba;
  }
  * { box-sizing: border-box; margin: 0; padding: 0; }
  html, body { width: 1200px; height: 904px; overflow: hidden; }
  body {
    background: var(--backdrop);
    font-family: "Open Sans", Arial, sans-serif;
    color: var(--text);
    display: flex;
    flex-direction: column;
    align-items: center;
    justify-content: center;
    gap: 30px;
  }
  .card {
    position: relative;
    width: 720px;
    height: 411px;
    background: var(--card);
    box-shadow: 0 6px 18px rgba(0,0,0,.18);
    overflow: hidden;
  }
  .firm-name {
    display: flex;
    align-items: center;
    gap: 14px;
    font-family: "Cinzel", Georgia, serif;
    font-weight: 500;
    color: var(--olive);
    letter-spacing: .04em;
  }
  .firm-mark {
    width: 34px; height: 34px;
    background: var(--olive);
    flex: none;
  }

  /* front */
  .card-front .firm-name {
    position: absolute;
    left: 190px; top: 150px;
    font-size: 26px;
  }
  .card-front .firm-mark { width: 44px; height: 44px; }
  .offices {
    position: absolute;
    left: 0; right: 0; top: 282px;
    text-align: center;
    font-size: 14px;
    letter-spacing: .06em;
    color: var(--text);
  }
  .offices .dot {
    display: inline-block;
    width: 7px; height: 7px;
    background: var(--olive);
    transform: rotate(45deg);
    margin: 0 12px 2px;
  }

  /* back */
  .card-back .firm-name {
    position: absolute;
    left: 40px; top: 92px;
    font-size: 20px;
  }
  .divider {
    position: absolute;
    left: 430px; top: 40px;
    width: 1px; height: 240px;
    background: var(--rule);
  }
  .locations {
    position: absolute;
    left: 452px; top: 44px;
    font-size: 13px;
    line-height: 1.45;
    color: var(--text);
  }
  .locations address { font-style: normal; margin-bottom: 14px; }
  .contact-line {
    display: flex; align-items: center; gap: 8px;
    font-size: 13px; line-height: 1.7;
  }
  .contact-line svg { width: 14px; height: 14px; fill: var(--olive); flex: none; }
  .person {
    position: absolute;
    left: 40px; top: 212px;
  }
  .person-name {
    font-size: 20px; font-weight: 600;
    color: var(--olive);
  }
  .person-title {
    font-size: 13px; color: var(--text-soft);
    margin-bottom: 8px;
  }
  .web-band {
    position: absolute;
    left: 0; right: 0; bottom: 30px;
    height: 34px;
    background: linear-gradient(90deg, var(--olive-light), var(--olive-dark) 45%);
    color: #fff;
    font-size: 15px;
    letter-spacing: .18em;
    display: flex; align-items: center; justify-content: flex-end;
    padding-right: 40px;
  }
  .web-band::before {
    content: "";
    position: absolute; left: 0; right: 0; top: -5px; height: 2px;
    background: var(--olive-light);
  }
</style>
</head>
<body>

<section class="card card-front">
  <div class="firm-name"><span class="firm-mark"></span>Taven &amp; Associates, PC</div>
  <p class="offices">Houston<span class="dot"></span>Sugar Land<span class="dot"></span>New York</p>
</section>

<section class="card card-back">
  <div class="firm-name"><span class="firm-mark"></span>Taven &amp; Associates, PC</div>
  <span class="divider"></span>

  <div class="locations">
    <address>482 W. Birchfield Ave.<br>Suite 318<br>Houston, TX 77391</address>
    <address>56 Marlow Creek Center Blvd.<br>Suite 240<br>Sugar Land, TX 77479</address>
    <p class="contact-line">
      <svg viewBox="0 0 16 16"><path d="M3.5 1l3 3-1.8 2a9 9 0 0 0 5.3 5.3l2-1.8 3 3-2 2C7 14 2 9 1.5 3z"/></svg>
      1-888-50-TAVEN
    </p>
    <p class="contact-line">
      <svg viewBox="0 0 16 16"><path d="M1 2h14v10H9v2h3v1H4v-1h3v-2H1zm1 1v8h12V3z"/></svg>
      lakeridgetrialcounsel.example
    </p>
  </div>

  <div class="person">
    <p class="person-name">Dorian M. Taven</p>
    <p class="person-title">Trial Attorney</p>
    <p class="contact-line">
      <svg viewBox="0 0 16 16"><path d="M3.5 1l3 3-1.8 2a9 9 0 0 0 5.3 5.3l2-1.8 3 3-2 2C7 14 2 9 1.5 3z"/></svg>
      713-555-0140
    </p>
    <p class="contact-line">
      <svg viewBox="0 0 16 16"><path d="M4 1h8v4H4zM1 6h14v6h-3v3H4v-3H1zm4 4v4h6v-4z"/></svg>
      713-555-0142
    </p>
    <p class="contact-line">
      <svg viewBox="0 0 16 16"><path d="M1 3h14v10H1zm1 1v.5l6 4 6-4V4zm0 2v6h12V6l-6 4z"/></svg>
      dorian.taven@tavenassociateslaw.example
    </p>
  </div>

  <div class="web-band">www.tavenassociateslaw.example</div>
</section>

</body>
</html>
```